Corvane Systems Modern, Sleek One Pager/Slick Sheet

Creative Brief: One-Pager Design for Corvane Systems
Project Overview:
We are seeking a highly skilled graphic designer to create a modern, sleek, and visually impactful one-pager (slick sheet) for Corvane Systems, a leading company in the defense and aerospace sector. This slick sheet will serve as a high-level marketing asset, designed to quickly capture attention and communicate Corvane Systems’s cutting-edge capabilities, technological expertise, and commitment to national security and innovation.
Key Objectives:
Establish a high-tech, sophisticated look and feel that aligns with the defense and aerospace industries.
Highlight Corvane Systems’s core competencies, key services, and differentiators with clear and concise messaging.
Ensure the design supports easy readability and quick scanning of critical information.
Incorporate strong visual hierarchy and premium, professional aesthetics.
Design Specifications:
Format: Single-page, print and digital distribution-ready (PDF format).
Layout Style: Clean, minimalist, and balanced with ample white space.
Typography: Modern, sans-serif fonts that convey innovation and strength.
Color Palette: Incorporate Corvane Systems’s brand colors (navy blue, steel gray, white, accents of metallic or deep reds if applicable).
Imagery: Use high-resolution imagery that reflects advanced technology, aerospace engineering, and national defense. Subtle technical graphics, schematics, or abstract patterns are acceptable to enhance visual interest without clutter.
Content Elements (To Be Provided):
Company Logo and Tagline
Key Capabilities and Service Offerings
Differentiators and Core Competencies
Contact Information
Visual Icons or Infographics for Quick Reference (if applicable)
Tone & Mood:
Professional, authoritative, and cutting-edge
Emphasizes trust, innovation, and mission-critical solutions
Appeals to government and defense industry stakeholders
Deliverables:
Final high-resolution print-ready PDF
Digital-friendly PDF optimized for email and web use
Source files (Adobe Illustrator, InDesign, or equivalent)
Target Market(s)
Defense/Aviation
Industry/Entity Type
Defense/Aviation
Look and feel

```html
<!DOCTYPE html>
<html lang="en">
<head>
<meta charset="utf-8">
<title>Corvane Systems — One Pager</title>
<link rel="stylesheet" href="https://fonts.googleapis.com/css2?family=Poppins:wght@400;500;600;700;800&display=swap">
<style>
:root{
  --stage:#e9eaee;
  --navy-deep:#0f1848;
  --navy:#1a2566;
  --navy-mid:#223079;
  --tile:#1d2868;
  --tile-edge:#2a3785;
  --steel:#b9bfcc;
  --steel-light:#d5d9e2;
  --glow:#4f8fe6;
  --white:#ffffff;
  --soft:#c9d3f2;
}
*{margin:0;padding:0;box-sizing:border-box}
html,body{width:1200px;height:625px;overflow:hidden;background:var(--stage);font-family:"Poppins",sans-serif}
.stage{width:1200px;height:625px;display:flex;justify-content:center;align-items:center}
.sheet{position:relative;width:438px;height:625px;overflow:hidden;color:var(--white);
  background:linear-gradient(180deg,var(--navy-deep) 0%,var(--navy) 45%,var(--navy-mid) 100%)}
.hero-art{position:absolute;left:0;top:0;width:438px;height:320px;
  background:
    radial-gradient(ellipse 60% 35% at 65% 28%,rgba(110,170,255,.55),rgba(60,110,220,.2) 55%,transparent 75%),
    radial-gradient(ellipse 30% 20% at 88% 15%,rgba(160,200,255,.35),transparent 70%),
    linear-gradient(180deg,#141e58 0%,#1a2566 100%)}
.deco-square{position:absolute;background:rgba(200,210,235,.35)}
.title{position:absolute;left:20px;top:160px;font-weight:800;font-size:28px;line-height:27px;letter-spacing:-.3px}
.subtitle{position:absolute;left:20px;top:217px;font-weight:500;font-size:14.5px;letter-spacing:.2px}
.oneliner{position:absolute;left:0;top:244px;width:237px;height:14px;background:var(--steel);
  clip-path:polygon(0 0,100% 0,96% 100%,0 100%);color:var(--navy-deep);font-size:8.6px;line-height:14px;padding-left:20px}
.section-head{font-weight:700;font-size:13.2px;line-height:15.5px;color:var(--steel-light)}
.section-head::after{content:"";display:block;width:50px;height:1.5px;background:var(--white);margin-top:5px}
.caps-head{position:absolute;left:20px;top:276px}
.caps-row{position:absolute;left:0;top:327px;width:438px;height:84px;display:flex;gap:2px;background:#141d55;padding-left:21px}
.cap-tile{width:98px;height:84px;background:var(--tile);border-left:1px solid var(--tile-edge);
  display:flex;flex-direction:column;align-items:center;justify-content:flex-start;padding-top:13px}
.cap-tile svg{width:34px;height:34px}
.cap-label{margin-top:9px;font-weight:600;font-size:6.9px;line-height:9px;text-align:center;text-transform:uppercase}
.lower{position:absolute;left:0;top:411px;width:438px;height:214px;
  background:radial-gradient(ellipse 50% 40% at 70% 40%,rgba(70,100,200,.25),transparent 70%)}
.diff{position:absolute;left:20px;top:428px}
.divider{position:absolute;left:210px;top:430px;width:1px;height:93px;background:var(--steel)}
.bullets{position:absolute;left:20px;top:468px;list-style:none;font-size:9.2px;line-height:15.2px}
.bullets li::before{content:"";display:inline-block;width:3px;height:3px;background:var(--steel);margin-right:5px;vertical-align:middle}
.why{position:absolute;left:252px;top:428px}
.why-text{position:absolute;left:252px;top:454px;width:175px;font-size:8.6px;line-height:10.8px}
.contact{position:absolute;left:20px;top:542px}
.contact .section-head::after{margin-top:4px}
.contact-list{position:absolute;left:20px;top:565px;list-style:none;font-size:9.2px;line-height:11px;font-weight:500}
.contact-list li{display:flex;align-items:center;gap:4px}
.contact-list svg{width:6px;height:6px;flex:none}
.brand{position:absolute;left:254px;top:556px;width:140px;display:flex;align-items:center;gap:6px}
.brand-mark{width:10px;height:10px;background:var(--white);flex:none}
.brand-name{font-weight:600;font-size:13px;letter-spacing:.5px;color:var(--white)}
</style>
</head>
<body>
<main class="stage">
  <article class="sheet">
    <div class="hero-art" role="img" aria-label="Glowing blue digital fighter jet illustration with light trails"></div>
    <span class="deco-square" style="left:26px;top:67px;width:26px;height:26px"></span>
    <span class="deco-square" style="left:26px;top:101px;width:15px;height:15px"></span>
    <span class="deco-square" style="left:402px;top:510px;width:14px;height:14px"></span>
    <span class="deco-square" style="left:388px;top:531px;width:26px;height:26px"></span>

    <h1 class="title">Mission Critical<br>Solutions.</h1>
    <p class="subtitle">FUTURE READY TECHNOLOGY.</p>
    <p class="oneliner">One-liner that supports your innovation edge</p>

    <h2 class="section-head caps-head">Key Capabilities and<br>Service Offerings</h2>

    <section class="caps-row">
      <div class="cap-tile">
        <svg viewBox="0 0 34 34" fill="none" stroke="#d5d9e2" stroke-width="2">
          <polygon points="17,3 29,10 29,24 17,31 5,24 5,10"/>
          <circle cx="17" cy="17" r="5"/><circle cx="17" cy="17" r="1.5" fill="#d5d9e2"/>
        </svg>
        <span class="cap-label">Cybersecurity<br>Operations</span>
      </div>
      <div class="cap-tile">
        <svg viewBox="0 0 34 34" fill="none" stroke="#d5d9e2" stroke-width="1.6">
          <line x1="5" y1="7" x2="29" y2="7"/><line x1="17" y1="3" x2="17" y2="12"/>
          <rect x="12" y="12" width="10" height="10" rx="3"/>
          <line x1="4" y1="18" x2="30" y2="18"/><line x1="17" y1="22" x2="17" y2="30"/>
        </svg>
        <span class="cap-label">Aerospace Systems<br>Integration</span>
      </div>
      <div class="cap-tile">
        <svg viewBox="0 0 34 34" fill="none" stroke="#d5d9e2" stroke-width="1.6">
          <rect x="3" y="4" width="28" height="21"/>
          <rect x="9" y="15" width="3" height="7" fill="#d5d9e2"/>
          <rect x="15" y="11" width="3" height="11" fill="#d5d9e2"/>
          <rect x="21" y="7" width="3" height="15" fill="#d5d9e2"/>
          <line x1="17" y1="25" x2="17" y2="30"/><line x1="11" y1="30" x2="23" y2="30"/>
        </svg>
        <span class="cap-label">Advanced Data<br>Analytics</span>
      </div>
      <div class="cap-tile">
        <svg viewBox="0 0 34 34" fill="none" stroke="#d5d9e2" stroke-width="1.6">
          <circle cx="18" cy="15" r="10"/><circle cx="18" cy="15" r="3.5"/>
          <line x1="4" y1="9" x2="9" y2="9"/><line x1="3" y1="15" x2="8" y2="15"/>
          <line x1="14" y1="25" x2="14" y2="31"/><line x1="22" y1="25" x2="22" y2="31"/>
        </svg>
        <span class="cap-label">AI &amp; Autonomous<br>Technologies</span>
      </div>
    </section>

    <div class="lower" aria-hidden="true"></div>

    <h2 class="section-head diff">Differentiators and<br>Core Competencies</h2>
    <ul class="bullets">
      <li>Proven past performance</li>
      <li>Security clearances</li>
      <li>Veteran-led teams</li>
      <li>Agile tech development</li>
    </ul>
    <span class="divider"></span>

    <h2 class="section-head why">Why Corvane Systems?</h2>
    <p class="why-text">A trusted partner with deep domain experties. we provide mission critical solutions leveraging cutting edge technology and innovation.</p>

    <div class="contact"><h2 class="section-head">Contact Us</h2></div>
    <ul class="contact-list">
      <li><svg viewBox="0 0 10 10"><path d="M2 1l2 2-1 1.5c.8 1.5 1.7 2.4 3 3L7.5 6l2 2-1.5 1.5C4.5 9 1 5.5.5 2z" fill="#d5d9e2"/></svg>202-555-0187</li>
      <li><svg viewBox="0 0 10 10"><rect x="1" y="2" width="8" height="6" fill="none" stroke="#d5d9e2"/><path d="M1 2l4 3.5L9 2" fill="none" stroke="#d5d9e2"/></svg>info@corvanesystems.com</li>
      <li><svg viewBox="0 0 10 10"><circle cx="5" cy="5" r="4" fill="none" stroke="#d5d9e2"/><line x1="1" y1="5" x2="9" y2="5" stroke="#d5d9e2"/></svg>www.corvanesystems.com</li>
    </ul>

    <div class="brand"><span class="brand-mark"></span><span class="brand-name">Corvane Systems</span></div>
  </article>
</main>
</body>
</html>
```